Illustrations for a Project Management Concept

we need illustrations for 5 project management principles that make up a holistic approach to project management, without all the BS. if we extract all the methodology, system, tool and mumbo-jumbo out of project management, we end up with some essential principles that are simple to understand and use. It's likely that people who use them will not be traditional Project Management types.

I've mocked up something that looks very corporate based on a template, but this has the wrong tone; the wrong feeling. I'd like something "funky" and colorful that conveys "Action" within "Simplicity".

the PPT file with the dark-blue background is the "corporate" consulting type mockup. the PPT with the white background shows an idea I had for breaking out each of the 5 principles (only one shown) to make it larger, with some text in a callout.

In the final deliverable, I need to be able to both show all 5 on one diagram, as well as slicing the image to display each principle separately. i do not have editing capabilities for vector image formats, only image formats

Reason: there are a number of designers who have only just accepted the invitation. I want to give everyone a chance to submit.

```html
<!DOCTYPE html>
<html lang="en">
<head>
<meta charset="utf-8">
<title>Five Principles Ring</title>
<link rel="stylesheet" href="https://fonts.googleapis.com/css2?family=Nunito:wght@800;900&display=swap">
<style>
  :root {
    --bg-blue: #1686b6;
    --grid-line: rgba(255, 255, 255, 0.06);
    --orange: #f8ae52;
    --pink: #de6286;
    --green: #1ab287;
    --salmon: #e8a67d;
    --hub: #6e6c71;
    --depth: #000000;
    --label: #ffffff;
  }
  html, body {
    margin: 0;
    padding: 0;
    overflow: hidden;
  }
  .canvas {
    width: 1200px;
    height: 848px;
    position: relative;
    overflow: hidden;
    background-color: var(--bg-blue);
    background-image:
      repeating-linear-gradient(0deg, var(--grid-line) 0 1px, transparent 1px 30px),
      repeating-linear-gradient(90deg, var(--grid-line) 0 1px, transparent 1px 30px);
  }
  .ring {
    position: absolute;
    inset: 0;
    width: 1200px;
    height: 848px;
  }
  .segment-depth { fill: var(--depth); }
  .segment--value { fill: var(--orange); }
  .segment--models { fill: var(--pink); }
  .segment--entropy { fill: var(--green); }
  .segment--threats { fill: var(--salmon); }
  .hub { fill: var(--hub); }
  .hub-depth { fill: var(--depth); }
  .label {
    font-family: "Nunito", sans-serif;
    font-weight: 900;
    font-size: 26px;
    fill: var(--label);
    text-anchor: middle;
    letter-spacing: 0.5px;
  }
  .label--hub { font-size: 29px; }
</style>
</head>
<body>
<main class="canvas">
  <svg class="ring" viewBox="0 0 1200 848" xmlns="http://www.w3.org/2000/svg" aria-label="Five project principles ring">
    <g class="ring-depth" transform="translate(589 436) scale(1 0.634)">
      <path class="segment-depth" d="M -355.1 205 A 410 410 0 0 1 -289.9 -289.9 L -137.9 -137.9 A 195 195 0 0 0 -168.9 97.5 Z"/>
      <path class="segment-depth" d="M -263.5 -314.1 A 410 410 0 0 1 355.1 -205 L 168.9 -97.5 A 195 195 0 0 0 -125.3 -149.4 Z"/>
      <path class="segment-depth" d="M 371.6 -173.3 A 410 410 0 0 1 235.2 335.9 L 111.9 159.7 A 195 195 0 0 0 176.7 -82.4 Z"/>
      <path class="segment-depth" d="M 205 355.1 A 410 410 0 0 1 -335.9 235.2 L -159.7 111.9 A 195 195 0 0 0 97.5 168.9 Z"/>
      <circle class="hub-depth" cx="0" cy="0" r="128"/>
    </g>
    <g class="ring-top" transform="translate(589 406) scale(1 0.634)">
      <path class="segment segment--threats" d="M -355.1 205 A 410 410 0 0 1 -289.9 -289.9 L -137.9 -137.9 A 195 195 0 0 0 -168.9 97.5 Z"/>
      <path class="segment segment--value" d="M -263.5 -314.1 A 410 410 0 0 1 355.1 -205 L 168.9 -97.5 A 195 195 0 0 0 -125.3 -149.4 Z"/>
      <path class="segment segment--models" d="M 371.6 -173.3 A 410 410 0 0 1 235.2 335.9 L 111.9 159.7 A 195 195 0 0 0 176.7 -82.4 Z"/>
      <path class="segment segment--entropy" d="M 205 355.1 A 410 410 0 0 1 -335.9 235.2 L -159.7 111.9 A 195 195 0 0 0 97.5 168.9 Z"/>
      <circle class="hub" cx="0" cy="-22" r="128"/>
    </g>

    <text class="label" transform="translate(655 190) rotate(12)">
      <tspan x="0" y="0">Fulfil Customer</tspan>
      <tspan x="0" y="30">Value</tspan>
    </text>
    <text class="label" transform="translate(865 425) rotate(72)">
      <tspan x="0" y="-15">Build Shared</tspan>
      <tspan x="0" y="15">Models</tspan>
    </text>
    <text class="label" transform="translate(530 578) rotate(9)">Suppres Entropy</text>
    <text class="label" transform="translate(292 370) rotate(-75)">
      <tspan x="0" y="-15">Eliminate Teaming</tspan>
      <tspan x="0" y="15">Threats</tspan>
    </text>
    <text class="label label--hub" transform="translate(591 375) rotate(8)">
      <tspan x="0" y="0">Achieve</tspan>
      <tspan x="0" y="32">Outcomes</tspan>
    </text>
  </svg>
</main>
</body>
</html>
```